Energy Infrastructure Business Card ReDesign

Looking to streamline our business card design for energy infrastructure company. Bring the design to a more clean but memorable business card. Currently being designed on gorlan cards and want a more professional, clean design. Don't love the Yellow but need to incorporate it in some fashion. Want the ability to easily update based on person / title for company around 300 people. Clean, modern, updated, memorable

Target Market(s)

Directors, Project Managers, Operations - Clients

Industry/Entity Type

Energy- Oil & Gas, Renewables, Utilities

Contact Information for Business Card

Name, Title, Company Name, Phone, Email, (option for second email), website , possible QR code to save contact information

Font styles to use
Sans Serif
Other font styles liked:
• Open

Requirements
Must have
• memorable design, clean, information about each person.
Nice to have
• QR code to save contacts, raised design,

```html
<!DOCTYPE html>
<html lang="en">
<head>
<meta charset="utf-8">
<title>Ridgeline Energy – Business Card</title>
<link href="https://fonts.googleapis.com/css2?family=Montserrat:wght@400;500;700&display=swap" rel="stylesheet">
<style>
  :root{
    --stage:#232323;
    --card:#1f2023;
    --ink-black:#09090a;
    --emboss:#2b2c30;
    --emboss-light:#3a3b40;
    --yellow:#f7e80f;
    --white:#f4f4f4;
  }
  *{box-sizing:border-box;margin:0;padding:0}
  html,body{width:1200px;height:780px;overflow:hidden;background:var(--stage)}
  body{font-family:"Montserrat",Arial,sans-serif;position:relative}

  .card{
    position:absolute;top:235px;width:540px;height:310px;
    background:var(--card);border-radius:22px;
    box-shadow:0 10px 24px rgba(0,0,0,.45);
    overflow:hidden;
  }
  .card--front{left:40px}
  .card--back{left:620px}

  .brand{
    position:absolute;font-weight:700;color:var(--ink-black);
    letter-spacing:.5px;line-height:1;white-space:nowrap;
  }
  .card--front .brand{left:0;right:0;top:78px;text-align:center;font-size:52px}
  .card--back .brand{left:34px;top:44px;font-size:32px}

  .tagline{
    position:absolute;left:0;right:0;bottom:54px;text-align:center;
    font-size:22px;font-weight:700;letter-spacing:3px;
    color:var(--emboss);
    text-shadow:0 1px 0 var(--emboss-light);
  }

  .person{position:absolute;right:52px;top:118px;text-align:right}
  .person__name{color:var(--yellow);font-weight:700;font-size:24px;line-height:1.15}
  .person__title{color:var(--white);font-weight:400;font-size:17px;margin-top:4px}
  .accent-bar{position:absolute;right:0;top:112px;width:22px;height:42px;background:var(--yellow)}

  .contacts{position:absolute;left:40px;bottom:34px;list-style:none}
  .contacts li{display:flex;align-items:center;gap:10px;color:var(--white);font-size:14px;line-height:1;margin-top:8px}
  .contacts svg{width:16px;height:14px;flex:none}
</style>
</head>
<body>

<section class="card card--front" aria-label="Card front">
  <div class="brand">Ridgeline Energy</div>
  <div class="tagline">SAFETY QUALITY PRODUCTION</div>
</section>

<section class="card card--back" aria-label="Card back">
  <div class="brand">Ridgeline Energy</div>

  <div class="person">
    <div class="person__name">Dana Whitfield</div>
    <div class="person__title">Managing Director</div>
  </div>
  <div class="accent-bar"></div>

  <ul class="contacts">
    <li>
      <svg viewBox="0 0 16 14" aria-hidden="true"><path fill="#f7e80f" d="M1 5c0-2 3-3 7-3s7 1 7 3v1h-3V4.5H4V6H1zM3 7h10l1 6H2z"/></svg>
      +916 555-0142
    </li>
    <li>
      <svg viewBox="0 0 16 14" aria-hidden="true"><rect x="1" y="2" width="14" height="10" fill="#f7e80f"/><path d="M1 2l7 6 7-6" stroke="#1f2023" stroke-width="1.4" fill="none"/></svg>
      dana@ridgelineco.com
    </li>
    <li>
      <svg viewBox="0 0 16 14" aria-hidden="true"><rect x="1" y="2" width="14" height="10" fill="#f7e80f"/><path d="M1 2l7 6 7-6" stroke="#1f2023" stroke-width="1.4" fill="none"/></svg>
      info@ridgelineco.com
    </li>
    <li>
      <svg viewBox="0 0 16 14" aria-hidden="true"><circle cx="8" cy="7" r="6" fill="#f7e80f"/><path d="M2 7h12M8 1c-3 3-3 9 0 12M8 1c3 3 3 9 0 12" stroke="#1f2023" stroke-width="1" fill="none"/></svg>
      www.ridgelineco.com
    </li>
  </ul>
</section>

</body>
</html>
```